Business Card cabinets and cabinets components making company.

the card should be formal and interesting at the same time. The main colors will be black and white.

Font styles to use
Sans Serif

Colors

Designer to choose only greyscale colors for use in the design.

Requirements
Must have
• At least must have the followings:
office phone
cell phone
address
position
name
email
web

```html
<!DOCTYPE html>
<html lang="en">
<head>
<meta charset="utf-8">
<title>Oakrow Business Card</title>
<link href="https://fonts.googleapis.com/css2?family=Mulish:wght@400;500;700&display=swap" rel="stylesheet">
<style>
  :root {
    --backdrop: #e4e2de;
    --card-light: #f3f3f5;
    --card-dark: #3a393b;
    --ink-brown: #3b2a1e;
    --ink-grey: #3a393b;
    --ink-white: #ffffff;
  }
  * { margin: 0; padding: 0; box-sizing: border-box; }
  html, body {
    width: 1131px; height: 1200px; overflow: hidden;
    background: var(--backdrop);
    font-family: "Mulish", sans-serif;
  }
  .canvas { position: relative; width: 1131px; height: 1200px; }
  .card {
    position: absolute; left: 214px; width: 780px; height: 448px;
  }
  .card--front { top: 56px; background: var(--card-light); color: var(--ink-grey); }
  .card--back { top: 601px; background: var(--card-dark); color: var(--ink-white); }

  .holder-name {
    position: absolute; left: 67px; top: 52px;
    font-size: 32px; font-weight: 500; color: var(--ink-brown); letter-spacing: 0.2px;
  }
  .holder-role {
    position: absolute; left: 67px; top: 92px;
    font-size: 19px; color: var(--ink-brown);
  }
  .divider {
    position: absolute; left: 67px; top: 134px; width: 90px; height: 2px;
    background: var(--ink-brown);
  }
  .address {
    position: absolute; left: 67px; top: 210px;
    font-size: 16.5px; line-height: 22px; font-style: normal;
  }
  .contacts {
    position: absolute; left: 67px; top: 302px; list-style: none;
    font-size: 16.5px; line-height: 22.5px;
  }
  .contacts li { display: flex; align-items: center; gap: 10px; }
  .contacts svg { width: 13px; height: 13px; fill: var(--ink-grey); flex: none; }

  .front-mark {
    position: absolute; left: 470px; top: 22px; width: 280px; height: 420px;
    display: flex; flex-direction: column; align-items: center; justify-content: center; gap: 34px;
  }
  .front-mark__square {
    width: 200px; height: 200px; background: var(--ink-grey);
  }
  .front-mark__name {
    font-size: 60px; font-weight: 700; color: var(--ink-grey); line-height: 1; letter-spacing: 1px;
  }

  .brand-name {
    position: absolute; left: 0; right: 0; top: 154px; text-align: center;
    font-size: 96px; font-weight: 700; letter-spacing: 1px; line-height: 1;
  }
  .brand-web {
    position: absolute; left: 0; right: 0; top: 398px; text-align: center;
    font-size: 18px; letter-spacing: 0.3px;
  }
</style>
</head>
<body>
<main class="canvas">
  <section class="card card--front">
    <h1 class="holder-name">Dana Whitlock</h1>
    <p class="holder-role">president</p>
    <div class="divider"></div>
    <address class="address">48 West 19th Street,<br>3rd FL New York,<br>NY 10011</address>
    <ul class="contacts">
      <li><svg viewBox="0 0 16 16"><path d="M3 1l3 3-2 2c1 2 3 4 6 6l2-2 3 3-2 2C7 15 1 9 1 3z"/></svg>(555) 214-7730</li>
      <li><svg viewBox="0 0 16 16"><path d="M1 6c0-3 14-3 14 0v1h-4V5H5v2H1zM3 8h10l1 7H2zm5 2a2 2 0 100 4 2 2 0 000-4z"/></svg>(555) 214-7731</li>
      <li><svg viewBox="0 0 16 16"><path d="M1 3h14v10H1zm1 1l6 5 6-5z"/></svg>dana@oakrowcabinetry.net</li>
      <li><svg viewBox="0 0 16 16"><circle cx="8" cy="8" r="7"/></svg>www.oakrowcabinetry.com</li>
    </ul>
    <div class="front-mark">
      <div class="front-mark__square"></div>
      <p class="front-mark__name">Oakrow</p>
    </div>
  </section>

  <section class="card card--back">
    <p class="brand-name">Oakrow</p>
    <p class="brand-web">www.oakrowcabinetry.com</p>
  </section>
</main>
</body>
</html>
```